Brovanta Business Card Design

Primarily a Real Estate Investment company but also invests in other business ventures.
Updates

The attachments have been uploaded to give you a better perspective on what I'm looking for. Please pay close attention to the Lark Stage Creations card as a sample.Thank you.

Target Market(s)

Upper escalante individuals that would like to purchase real estate

Industry/Entity Type

Business

Contact Information for Business Card

Brovanta Holdings LLC, Danela R. Hartwick, CEO/MBA, 310-555-0147, Danela4816@mailbrook.example

Colors
0455a3
ffffff

Requirements
Must have
• Majority of card color MUST be Black ----- Like pictures 2&3
(pic4) Raised silver foil "B" to start the Brovanta name on the card.
(pic3) Love the whole layout, round edges, placement of contact info. {It is clean and elegant}
(pic1) Matte & Gloss backing
(pic2) Blue color (maybe the remainder of company name to make the card have pop of color).
Nice to have
• Silver foil siding

```html
<!DOCTYPE html>
<html lang="en">
<head>
<meta charset="utf-8">
<title>Brovanta Holdings – Business Card</title>
<link rel="stylesheet" href="https://fonts.googleapis.com/css2?family=Great+Vibes&family=Montserrat:wght@400;500&display=swap">
<style>
  :root {
    --backdrop: #d8d8d6;
    --card-black: #141414;
    --card-white: #f7f7f5;
    --brand-blue: #0455a3;
    --silver: #e4e4e4;
    --ink-grey: #4a4a4a;
  }
  * { box-sizing: border-box; margin: 0; padding: 0; }
  html, body {
    width: 1200px;
    height: 818px;
    overflow: hidden;
    background: var(--backdrop);
  }
  .sheet {
    position: relative;
    width: 1200px;
    height: 818px;
    display: flex;
    align-items: center;
    justify-content: center;
    gap: 60px;
  }
  .card {
    position: relative;
    width: 500px;
    height: 286px;
    border-radius: 18px;
    overflow: hidden;
    box-shadow: 0 10px 24px rgba(0, 0, 0, 0.18);
  }

  /* Front: black */
  .card-front {
    background: var(--card-black);
    display: flex;
    flex-direction: column;
    align-items: center;
    justify-content: center;
  }
  .front-mark {
    display: flex;
    align-items: center;
    gap: 16px;
  }
  .mark-circle {
    width: 62px;
    height: 62px;
    border: 3px solid var(--silver);
    border-radius: 50%;
  }
  .front-name {
    font-family: "Great Vibes", cursive;
    font-size: 56px;
    color: var(--silver);
    line-height: 1;
  }
  .front-tagline {
    margin-top: 20px;
    font-family: "Great Vibes", cursive;
    font-size: 28px;
    color: var(--silver);
  }

  /* Back: white */
  .card-back {
    background: var(--card-white);
    display: flex;
    padding: 34px 36px;
  }
  .back-brand {
    width: 170px;
    display: flex;
    flex-direction: column;
    align-items: center;
    justify-content: flex-end;
    padding-bottom: 20px;
  }
  .brand-circle {
    width: 64px;
    height: 64px;
    border: 3px solid var(--brand-blue);
    border-radius: 50%;
    margin-bottom: 12px;
  }
  .brand-name {
    font-family: "Great Vibes", cursive;
    font-size: 34px;
    color: var(--brand-blue);
    line-height: 1;
  }
  .back-details {
    flex: 1;
    display: flex;
    flex-direction: column;
    justify-content: center;
    padding-left: 20px;
  }
  .person-name {
    font-family: "Great Vibes", cursive;
    font-size: 36px;
    color: var(--brand-blue);
    line-height: 1.1;
  }
  .person-title {
    font-family: "Montserrat", sans-serif;
    font-size: 11px;
    letter-spacing: 2px;
    color: var(--ink-grey);
    margin: 4px 0 18px;
  }
  .contact-list {
    list-style: none;
    font-family: "Montserrat", sans-serif;
    font-size: 11.5px;
    color: var(--ink-grey);
  }
  .contact-list li {
    display: flex;
    align-items: center;
    gap: 8px;
    margin-bottom: 8px;
  }
  .contact-icon {
    width: 13px;
    height: 13px;
    flex: none;
  }
</style>
</head>
<body>
<main class="sheet">
  <section class="card card-front" aria-label="Card front">
    <div class="front-mark">
      <span class="mark-circle"></span>
      <span class="front-name">Brovanta</span>
    </div>
    <p class="front-tagline">Brovanta Holdings LLC</p>
  </section>

  <section class="card card-back" aria-label="Card back">
    <div class="back-brand">
      <span class="brand-circle"></span>
      <span class="brand-name">Brovanta</span>
    </div>
    <div class="back-details">
      <h1 class="person-name">Danela R. Hartwick</h1>
      <p class="person-title">CEO / MBA</p>
      <ul class="contact-list">
        <li>
          <svg class="contact-icon" viewBox="0 0 24 24" aria-hidden="true"><path fill="#0455a3" d="M6.6 10.8a15.1 15.1 0 0 0 6.6 6.6l2.2-2.2c.3-.3.7-.4 1-.2 1.1.4 2.3.6 3.6.6.6 0 1 .4 1 1V20c0 .6-.4 1-1 1A17 17 0 0 1 3 4c0-.6.4-1 1-1h3.5c.6 0 1 .4 1 1 0 1.3.2 2.5.6 3.6.1.3 0 .7-.2 1z"/></svg>
          310-555-0147
        </li>
        <li>
          <svg class="contact-icon" viewBox="0 0 24 24" aria-hidden="true"><path fill="#0455a3" d="M3 5h18v14H3z"/><path fill="none" stroke="#f7f7f5" stroke-width="1.8" d="M3.5 6l8.5 7 8.5-7"/></svg>
          Danela4816@mailbrook.example
        </li>
        <li>
          <svg class="contact-icon" viewBox="0 0 24 24" aria-hidden="true"><path fill="#0455a3" d="M12 3l9 8h-3v9h-5v-6h-2v6H6v-9H3z"/></svg>
          Real Estate &amp; Ventures
        </li>
      </ul>
    </div>
  </section>
</main>
</body>
</html>
```